Marlow Hire Business Card for recruitment company

We are looking for a Business Card Design that incorporates our personal details and our busines name and logo. We are a specialized search consultancy that recruit Property and Construction professionals.
We would like a business card that stands out and is appealing to the Construction and Property industry as well.

Target Market(s)

people in the construction and property industry

Contact Information for Business Card

Business Name and logo

Font styles to use
Serif

Colors
0094D4
00A9DD
6FCCEA
C7EBF8
E9F6FB

Requirements
Must have
• Business name and logo as well as contact details
Should not have
• No photos of us please

```html
<!DOCTYPE html>
<html lang="en">
<head>
<meta charset="utf-8">
<title>Marlow Hire – Business Card</title>
<link rel="stylesheet" href="https://fonts.googleapis.com/css2?family=Lora:wght@400;500;600;700&display=swap">
<style>
  :root {
    --blue-deep: #0094d4;
    --blue-mid: #00a9dd;
    --blue-soft: #6fccea;
    --blue-pale: #c7ebf8;
    --blue-mist: #e9f6fb;
    --paper: #ffffff;
    --shadow: rgba(0, 80, 120, 0.22);
  }
  * { box-sizing: border-box; margin: 0; padding: 0; }
  html, body { width: 1200px; height: 1200px; overflow: hidden; }
  body {
    background: var(--blue-pale);
    font-family: "Lora", Georgia, serif;
    position: relative;
  }
  .card {
    position: absolute;
    left: 288px;
    width: 623px;
    height: 366px;
    border-radius: 28px;
    box-shadow: 0 4px 10px var(--shadow);
    overflow: hidden;
  }
  .card-front { top: 188px; background: var(--paper); color: var(--blue-deep); }
  .card-back  { top: 643px; background: var(--blue-deep); color: var(--paper); }

  .holder { position: absolute; left: 37px; top: 90px; }
  .holder-name { font-size: 29px; font-weight: 700; line-height: 1; }
  .holder-role { font-size: 15px; font-weight: 400; margin-top: 5px; color: var(--blue-mid); }

  .contact-list { position: absolute; left: 41px; top: 173px; list-style: none; }
  .contact-list li {
    display: flex; align-items: flex-start;
    font-size: 15px; font-weight: 600; line-height: 20px;
  }
  .contact-list svg { width: 14px; height: 14px; margin: 3px 9px 0 0; flex: none; }
  .contact-list .number { font-weight: 500; }

  .brand-front {
    position: absolute; left: 386px; top: 82px; width: 188px; height: 225px;
    display: flex; align-items: center; justify-content: center;
    text-align: center; font-size: 34px; font-weight: 600; line-height: 1.1;
    color: var(--blue-deep);
  }

  .brand-back {
    position: absolute; inset: 0;
    display: flex; align-items: center; justify-content: center;
    font-size: 52px; font-weight: 500; letter-spacing: 4px;
    text-transform: uppercase; padding-top: 8px;
  }
</style>
</head>
<body>
  <section class="card card-front">
    <div class="holder">
      <h1 class="holder-name">Odette Rayner</h1>
      <p class="holder-role">CEO Equal Opportunity Consultant</p>
    </div>
    <ul class="contact-list">
      <li><svg viewBox="0 0 24 24" fill="#0094d4"><path d="M6.6 10.8a15 15 0 0 0 6.6 6.6l2.2-2.2c.3-.3.7-.4 1-.2 1.1.4 2.3.6 3.6.6.6 0 1 .4 1 1V20c0 .6-.4 1-1 1C10.6 21 3 13.4 3 4c0-.6.4-1 1-1h3.5c.6 0 1 .4 1 1 0 1.3.2 2.5.6 3.6.1.3 0 .7-.2 1z"/></svg><span><span class="number">555-014-2287.</span> (Office)</span></li>
      <li><svg viewBox="0 0 24 24"><rect x="2" y="5" width="20" height="14" fill="#0094d4"/><path d="M2 5l10 8 10-8" fill="none" stroke="#ffffff" stroke-width="1.6"/></svg><span>info@marlowhire.com</span></li>
      <li><svg viewBox="0 0 24 24"><circle cx="12" cy="12" r="9" fill="none" stroke="#0094d4" stroke-width="2"/><path d="M3 12h18M12 3c3 3 3 15 0 18M12 3c-3 3-3 15 0 18" fill="none" stroke="#0094d4" stroke-width="1.6"/></svg><span>www.marlowhire.com</span></li>
      <li><svg viewBox="0 0 24 24" fill="#0094d4"><path d="M12 2a7 7 0 0 0-7 7c0 5 7 13 7 13s7-8 7-13a7 7 0 0 0-7-7zm0 9.5A2.5 2.5 0 1 1 12 6.5a2.5 2.5 0 0 1 0 5z"/></svg><span>4410 Larkspur Avenue Suite 210<br>Fairview, KS 66020</span></li>
    </ul>
    <div class="brand-front">Marlow Hire</div>
  </section>

  <section class="card card-back">
    <div class="brand-back">Marlow Hire</div>
  </section>
</body>
</html>
```